Real Estate Agent needs a Postcard Design

I need a postcard design for a marketing campaign in a specific area where I just sold 3 listings and they are all the highest sales in that community (Evergreen in San Jose, CA). The design should include my information, my picture, logo and the information on the 3 properties that I just sold.
5162 Brantley Street in San Jose CA, sold for $810,000
5148 Brantley Street in San Jose CA, sold for $816,000
5196 Brantley Street in San Jose CA sold for $820,488

I am attaching pictures of the properties, my picture, and the company logo. Also I am attaching a sample of another postcard we used for another campaign. I need the front and back images of the postcards sent separately in jpeg format saved with a 300 DPI for best print resolution and also I would like to have a file that I can modify in case I want to add or delete any of the information.
Thank you and please contact me with questions.

```html
<!DOCTYPE html>
<html lang="en">
<head>
<meta charset="utf-8">
<title>Hartwell Homes Postcard – Front and Back</title>
<link rel="stylesheet" href="https://fonts.googleapis.com/css2?family=Source+Sans+3:wght@400;600;700&family=Oswald:wght@500&family=Libre+Baskerville&display=swap">
<style>
:root{
  --brand-red:#b41f24;
  --ink:#231f20;
  --label-dark:rgba(40,40,40,.82);
  --paper:#ffffff;
  --backdrop:#e6e6e6;
  --rule:#333333;
  --photo-sky:#b9cfe3;
  --photo-wall:#d9c9b2;
  --photo-green:#7f9a5a;
  --portrait:#8a7d6c;
}
*{box-sizing:border-box;margin:0;padding:0}
html,body{width:1200px;height:1000px;overflow:hidden}
body{background:var(--backdrop);position:relative;font-family:"Source Sans 3",Arial,sans-serif;color:var(--ink)}
.card{position:absolute;width:621px;height:401px;background:var(--paper);overflow:hidden}
.card--front{left:114px;top:66px}
.card--back{left:481px;top:516px}
.abs{position:absolute}

/* photo placeholders */
.photo{position:absolute}
.photo--house{background:linear-gradient(180deg,var(--photo-sky) 0%,var(--photo-sky) 25%,var(--photo-wall) 45%,var(--photo-wall) 75%,var(--photo-green) 100%)}
.photo--portrait{background:linear-gradient(180deg,#b9a98f 0%,var(--portrait) 55%,#2a2f3a 100%)}

/* front */
.headline{left:24px;top:0;width:302px;height:58px;background:var(--brand-red);color:#fff;text-align:center;padding-top:3px}
.headline__main{font-weight:700;font-size:26px;letter-spacing:.5px;line-height:30px}
.headline__sub{font-size:17px;letter-spacing:.4px;line-height:20px}
.sold-label{position:absolute;background:var(--label-dark);color:#fff;padding:3px 8px}
.sold-label__addr{font-size:9.5px;line-height:12px}
.sold-label__row{display:flex;align-items:baseline;gap:6px}
.sold-label__tag{font-weight:700;font-size:11px}
.sold-label__price{font-family:"Libre Baskerville",Georgia,serif;font-size:20px;line-height:24px}
.contact-band{left:0;top:289px;width:126px;height:92px;background:var(--brand-red)}
.contact-box{left:126px;top:289px;width:293px;height:92px;background:var(--brand-red);color:#fff;padding:10px 0 0 18px}
.contact-box__name{font-weight:700;font-size:26px;letter-spacing:.5px;line-height:28px}
.contact-box__phone{font-weight:600;font-size:21px;line-height:26px}
.contact-box__links{font-size:11.5px;margin-top:6px}
.brand{display:flex;align-items:center;gap:6px;color:var(--brand-red);font-weight:700;white-space:nowrap}
.brand__mark{background:var(--brand-red)}

/* back */
.promise{left:192px;top:10px;width:215px;height:71px;background:var(--brand-red);color:#fff;font-family:"Oswald",Arial,sans-serif;font-size:10px;text-align:center;line-height:19.5px;padding-top:6px;letter-spacing:.2px}
.program-tag{top:99px;height:22px;font-weight:700;font-size:10.5px;text-align:center;line-height:22px;color:#fff}
.program-tag--seller{left:26px;width:153px;background:var(--ink)}
.program-tag--buyer{left:224px;width:154px;background:var(--brand-red)}
.program-panel{top:117px;height:95px}
.program-panel--seller{left:0;width:230px;background:var(--brand-red);clip-path:polygon(0 0,200px 0,230px 100%,0 100%)}
.program-panel--buyer{left:198px;width:210px;background:var(--ink);clip-path:polygon(0 0,100% 0,100% 100%,32px 100%)}
.program-text{position:absolute;color:#fff;font-size:9.5px;line-height:11px;text-align:center}
.program-text p{margin-bottom:6px}
.agent-info{left:156px;top:302px;font-size:12.5px;line-height:16px}
.agent-info__name{font-weight:700;font-size:17px;letter-spacing:.5px;line-height:20px}
.stamp{left:516px;top:16px;width:80px;height:90px;border:1px solid var(--rule)}
.address-line{left:433px;width:167px;height:1px;background:var(--rule)}
</style>
</head>
<body>

<!-- FRONT -->
<section class="card card--front">
  <div class="photo photo--house" style="left:8px;top:10px;width:344px;height:379px" role="img" aria-label="Photo of the two-storey townhouse at 5196 Brantley Street"></div>
  <div class="photo photo--house" style="left:360px;top:10px;width:252px;height:154px" role="img" aria-label="Photo of the townhouse at 5148 Brantley Street"></div>
  <div class="photo photo--house" style="left:360px;top:174px;width:252px;height:155px" role="img" aria-label="Photo of the townhouse at 5162 Brantley Street"></div>

  <div class="abs headline">
    <div class="headline__main">LET ME HELP YOU!</div>
    <div class="headline__sub">WHETHER BUYING OR SELLING</div>
  </div>

  <div class="sold-label" style="left:0;top:211px;width:171px">
    <div class="sold-label__addr">5196 Brantley Street in San Jose CA</div>
    <div class="sold-label__row"><span class="sold-label__tag">SOLD for</span><span class="sold-label__price">$820,488</span></div>
  </div>
  <div class="sold-label" style="left:450px;top:103px;width:171px">
    <div class="sold-label__addr">5148 Brantley Street in San Jose CA</div>
    <div class="sold-label__row"><span class="sold-label__tag">SOLD for</span><span class="sold-label__price">$816,000</span></div>
  </div>
  <div class="sold-label" style="left:450px;top:272px;width:171px">
    <div class="sold-label__addr">5162 Brantley Street in San Jose CA</div>
    <div class="sold-label__row"><span class="sold-label__tag">SOLD for</span><span class="sold-label__price">$810,000</span></div>
  </div>

  <div class="abs contact-band"></div>
  <div class="photo photo--portrait" style="left:22px;top:272px;width:104px;height:129px" role="img" aria-label="Portrait photo of agent Daniel Orvella"></div>
  <div class="abs contact-box">
    <div class="contact-box__name">DANIEL ORVELLA</div>
    <div class="contact-box__phone">Call: +1 415-555-0182</div>
    <div class="contact-box__links">daniel@hartwellhomes.com | www.hartwellhomes.com</div>
  </div>

  <div class="abs brand" style="left:458px;top:356px;font-size:20px">
    <span class="brand__mark" style="width:14px;height:14px"></span>Hartwell Homes
  </div>
</section>

<!-- BACK -->
<section class="card card--back">
  <div class="abs brand" style="left:12px;top:38px;font-size:21px">
    <span class="brand__mark" style="width:15px;height:15px"></span>Hartwell Homes
  </div>

  <div class="abs promise">
    <div>MOST COMPETITIVE RATE</div>
    <div>PERSONALIZED COSTUMER SERVICED</div>
    <div>WE SELL HOME FAST AT A FAIR MARKET VALUE</div>
  </div>

  <div class="abs program-panel program-panel--seller"></div>
  <div class="abs program-panel program-panel--buyer"></div>
  <div class="abs program-tag program-tag--seller">SELLER DISCOUNT PROGRAM</div>
  <div class="abs program-tag program-tag--buyer">BUYER DISCOUNT PROGRAM</div>

  <div class="program-text" style="left:22px;top:128px;width:170px">
    <p>When you list your home for sale with Hartwell Homes Inc. You will pay less in real estate comission, saving thousand of dollars.</p>
    <p>Wouldn't you rather pay 4% commission than the consumary 5% to 6%?</p>
  </div>
  <div class="program-text" style="left:212px;top:128px;width:190px">
    <p>when you BUY a home you will receive a commision rebate 50% of the commision.</p>
    <p>Example based on 3% commission:<br>Receiver by the buyer broker</p>
    <p>800K Home purchase =<br>$12000 Cash Rebate</p>
  </div>

  <div class="photo photo--portrait" style="left:22px;top:234px;width:118px;height:148px" role="img" aria-label="Portrait photo of agent Daniel Orvella"></div>
  <div class="abs agent-info">
    <div class="agent-info__name">DANIEL ORVELLA</div>
    <div>BRE Licence #02918364</div>
    <div>Email: daniel@hartwellhomes.com</div>
    <div>Call: +1 415-555-0182</div>
    <div>www.hartwellhomes.com</div>
  </div>

  <div class="abs stamp"></div>
  <div class="abs address-line" style="top:201px"></div>
  <div class="abs address-line" style="top:234px"></div>
  <div class="abs address-line" style="top:266px"></div>
  <div class="abs address-line" style="top:299px"></div>
</section>

</body>
</html>
```